Website Front Page Banner Design for High Technology Intellectual Property

Develop Graphical Hero Banner to be used on the main page of Veltrona .com. The banner will promote the availability of Veltrona JESD204C IP (Intellectual Property). Please see attached pdf doc and follow details for Static Banner. We are looking for a Banner that is visually attention grabbing and uses imagery of applications that are enabled by the IP we are promoting (Applications such as 5G Wireless Infrastructure, CT/MRI/Ultrasound medical equipment, Radar / LIDAR / Satellites and High-Speed Test and Measurement equipment for a few examples). It would be good if the banner generally follow our color template of Green, White and Black - but the images of applications can use additional colors. Additonally, to learn more about JESD204 - recommend going to the following sites to understand what this IP is used for and what markets it address - additionally, I am open to answer any questions you may have. Sites: https://www.quarnify-tech.com/blog/high-speed-interface/jesd204c/, https://resources.pendrelo.com/p/what-jesd204c-standard-adcs,
Target Market(s)
Various High Technology Markets such as Defense, Medical, Test and Measurement, Industrial / Robotics, Wireless Communications
Industry/Entity Type
Semiconductor
Look and feel

```html
<!DOCTYPE html>
<html lang="en">
<head>
<meta charset="UTF-8">
<title>Veltrona JESD204C IP Core – Hero Banner</title>
<link href="https://fonts.googleapis.com/css2?family=Poppins:wght@400;500;600;700&display=swap" rel="stylesheet">
<style>
  :root {
    --green: #1ec43f;
    --green-deep: #0f8a2a;
    --green-dark: #06361a;
    --ink: #030805;
    --band: rgba(4, 10, 6, 0.94);
    --white: #ffffff;
    --muted: #d9e6dc;
  }
  * { box-sizing: border-box; margin: 0; padding: 0; }
  html, body { width: 1200px; height: 600px; overflow: hidden; background: var(--ink); }
  .banner {
    position: relative;
    width: 1200px;
    height: 600px;
    overflow: hidden;
    font-family: 'Poppins', sans-serif;
    color: var(--white);
    background: var(--ink);
  }
  .hero-visual {
    position: absolute;
    inset: 0;
    background:
      radial-gradient(ellipse 260px 340px at 1080px 230px, rgba(40, 210, 70, 0.55), transparent 70%),
      radial-gradient(ellipse 200px 300px at 760px 260px, rgba(30, 160, 60, 0.35), transparent 70%),
      radial-gradient(ellipse 520px 90px at 620px 440px, rgba(40, 200, 70, 0.35), transparent 70%),
      linear-gradient(90deg, #020604 0%, #06180c 35%, #0b3317 60%, #0c4a1d 80%, #0a3a17 100%);
  }
  .hero-shade {
    position: absolute;
    inset: 0;
    background: linear-gradient(90deg, rgba(2, 6, 4, 0.85) 0%, rgba(2, 6, 4, 0.55) 40%, rgba(2, 6, 4, 0) 70%);
  }
  .ribbon {
    position: absolute;
    left: 60px;
    top: 0;
    width: 94px;
    height: 89px;
    background: var(--green-deep);
    clip-path: polygon(0 0, 100% 0, 100% 100%, 50% 80%, 0 100%);
    text-align: center;
    padding-top: 16px;
    font-weight: 700;
    line-height: 1;
  }
  .ribbon-big { display: block; font-size: 20px; letter-spacing: 0.5px; }
  .ribbon-small { display: block; font-size: 13px; margin-top: 6px; letter-spacing: 0.3px; }
  .headline {
    position: absolute;
    left: 59px;
    top: 140px;
    font-weight: 700;
    text-transform: uppercase;
  }
  .headline-line { display: block; font-size: 38px; line-height: 50px; letter-spacing: 1.2px; }
  .headline-product { display: block; margin-top: 6px; line-height: 1; }
  .product-code { color: var(--green); font-size: 57px; letter-spacing: 1px; }
  .product-kind { font-size: 32px; margin-left: 14px; letter-spacing: 0.5px; }
  .rule {
    position: absolute;
    left: 60px;
    top: 307px;
    width: 360px;
    height: 1px;
    background: linear-gradient(90deg, var(--green) 0%, rgba(30, 196, 63, 0.6) 60%, transparent 100%);
  }
  .intro {
    position: absolute;
    left: 60px;
    top: 322px;
    font-size: 14.5px;
    line-height: 23px;
    color: var(--muted);
  }
  .intro strong { color: var(--green); font-weight: 600; }
  .cta {
    position: absolute;
    left: 60px;
    top: 413px;
    width: 139px;
    height: 38px;
    border-radius: 19px;
    background: var(--green);
    display: flex;
    align-items: center;
    padding-left: 20px;
    font-size: 13px;
    color: var(--white);
    text-decoration: none;
  }
  .cta-icon {
    position: absolute;
    right: 3px;
    top: 3px;
    width: 32px;
    height: 32px;
  }
  .feature-band {
    position: absolute;
    left: 0;
    top: 517px;
    width: 1200px;
    height: 83px;
    background: var(--band);
    border-top: 1px solid rgba(255, 255, 255, 0.18);
  }
  .band-divider-svg { position: absolute; left: 0; top: 517px; width: 1200px; height: 83px; }
  .feature { position: absolute; top: 535px; }
  .feature-icon { position: absolute; left: 0; top: 3px; width: 34px; height: 34px; }
  .feature-title {
    position: absolute;
    top: 0;
    white-space: nowrap;
    font-size: 14px;
    font-weight: 500;
    letter-spacing: 0.4px;
    text-transform: uppercase;
  }
  .feature-text {
    position: absolute;
    top: 20px;
    white-space: nowrap;
    font-size: 11px;
    line-height: 15px;
    color: var(--muted);
  }
  .feature-sep {
    position: absolute;
    top: 535px;
    width: 1px;
    height: 47px;
    background: rgba(255, 255, 255, 0.2);
  }
  .tagline {
    position: absolute;
    left: 904px;
    top: 538px;
    font-size: 18px;
    font-weight: 600;
    line-height: 23px;
    letter-spacing: 0.6px;
    text-transform: uppercase;
  }
  .tagline-accent { color: var(--green); }
</style>
</head>
<body>
<main class="banner">
  <div class="hero-visual" role="img" aria-label="Dark data-center aisle with green-lit server racks and streaks of green light suggesting high-speed data flow"></div>
  <div class="hero-shade"></div>

  <div class="ribbon">
    <span class="ribbon-big">NOW</span>
    <span class="ribbon-small">AVAILABLE!</span>
  </div>

  <h1 class="headline">
    <span class="headline-line">High-Perfomance</span>
    <span class="headline-line">Data Connectivity</span>
    <span class="headline-product"><span class="product-code">JESD204C</span><span class="product-kind">IP Core</span></span>
  </h1>
  <div class="rule"></div>

  <p class="intro">
    Industry-Leading Efficiency For Next-Gen ADCs, DACs,<br>
    And Veltrona FGPAs. Support For High Line Rates<br>
    Up To <strong>32.5 Gbps.</strong>
  </p>

  <a class="cta" href="#">Learn More
    <svg class="cta-icon" viewBox="0 0 32 32" aria-hidden="true">
      <circle cx="16" cy="16" r="15" fill="#ffffff"/>
      <circle cx="16" cy="16" r="11.5" fill="none" stroke="#1ec43f" stroke-width="2"/>
      <path d="M10 16h11M17 11.5l4.5 4.5-4.5 4.5" fill="none" stroke="#1ec43f" stroke-width="2.4" stroke-linecap="round" stroke-linejoin="round"/>
    </svg>
  </a>

  <div class="feature-band"></div>
  <svg class="band-divider-svg" viewBox="0 0 1200 83" aria-hidden="true">
    <path d="M838 0 L852 14 L873 0" fill="none" stroke="rgba(255,255,255,0.25)" stroke-width="1"/>
    <path d="M873 0 L790 83" fill="none" stroke="#1ec43f" stroke-width="1"/>
  </svg>

  <div class="feature" style="left:60px">
    <svg class="feature-icon" viewBox="0 0 34 34" aria-hidden="true">
      <path d="M5 25a13 13 0 1 1 24 0" fill="none" stroke="#1ec43f" stroke-width="4" stroke-linecap="round"/>
      <path d="M17 21l7-9" stroke="#1ec43f" stroke-width="3" stroke-linecap="round"/>
      <circle cx="17" cy="21" r="3" fill="#1ec43f"/>
      <rect x="10" y="28" width="14" height="2" fill="#1ec43f"/>
    </svg>
    <div class="feature-title" style="left:42px">High Performance</div>
    <div class="feature-text" style="left:42px">Optimized for ultra-high-speed<br>data transfer.</div>
  </div>
  <div class="feature-sep" style="left:290px"></div>

  <div class="feature" style="left:306px">
    <svg class="feature-icon" viewBox="0 0 34 34" aria-hidden="true">
      <path d="M6 12a13 13 0 1 1 0 10" fill="none" stroke="#1ec43f" stroke-width="3.5"/>
      <path d="M1 20l5 6 5-6z" fill="#1ec43f"/>
      <circle cx="19" cy="17" r="9" fill="#1ec43f"/>
      <path d="M19 11v6l4 3" fill="none" stroke="#030805" stroke-width="2" stroke-linecap="round"/>
    </svg>
    <div class="feature-title" style="left:48px">Low Latency</div>
    <div class="feature-text" style="left:48px">Designed for minimal latency<br>and maximum efficiency.</div>
  </div>
  <div class="feature-sep" style="left:531px"></div>

  <div class="feature" style="left:548px">
    <svg class="feature-icon" viewBox="0 0 34 34" aria-hidden="true">
      <rect x="12" y="2" width="21" height="22" fill="#1ec43f"/>
      <path d="M20 16l9-9M23 7h6v6" fill="none" stroke="#030805" stroke-width="1.8"/>
      <rect x="1" y="12" width="20" height="7" rx="1" fill="#1ec43f" stroke="#030805" stroke-width="1"/>
      <rect x="1" y="20" width="20" height="7" rx="1" fill="#1ec43f" stroke="#030805" stroke-width="1"/>
      <rect x="1" y="28" width="20" height="5" rx="1" fill="#1ec43f" stroke="#030805" stroke-width="1"/>
      <circle cx="5" cy="15.5" r="1" fill="#030805"/>
      <circle cx="5" cy="23.5" r="1" fill="#030805"/>
    </svg>
    <div class="feature-title" style="left:49px">Scalable For The Future</div>
    <div class="feature-text" style="left:49px">Built to meet the demands of<br>next-generation systems.</div>
  </div>

  <div class="tagline">
    Built For Today.<br>
    <span class="tagline-accent">Ready For Tomorrow.</span>
  </div>
</main>
</body>
</html>
```